Halvern Properties Business Cards

I would like a business card that includes myself and my partner.
Includes: Logo, office #, email, website, our names, our numbers and possibly the address. I would also like the logo to be embossed and the card to be horizontal.
There is a photo of our yard signs to give you an idea of the colors of our business.

Target Market(s)

Everyone in real estate market.
We are in a rural area. Our clientele are from all socioeconomic backgrounds.

Industry/Entity Type

Real Estate Agent

Contact Information for Business Card

Company Name: Halvern Properties
Our Names, Titles & Cell #'s : Marla Halvern-Broker (555).316.4827, Tessa Halvern-Realtor (555).627.9154
Office #: (555).841.2600
Website: halvernproperties-example.com
Joint Email: halvern@halvernproperties-example.com
Office Address: 518B W. Cottonwell Ave.
Cedar Hollow, TX. 70999

Font styles to use
Serif

Requirements
Must have
• HORIZONTAL, Logo, Myself and my partners names, Our cell #'s, our office #, our website, our email address
Nice to have
• Embossed logo, office address, our titles.

```html
<!DOCTYPE html>
<html lang="en">
<head>
<meta charset="utf-8">
<title>Halvern Properties – Business Card</title>
<link rel="stylesheet" href="https://fonts.googleapis.com/css2?family=Open+Sans:wght@400;600&display=swap">
<style>
  :root {
    --page-bg: #e9e6ea;
    --card-bg: #ffffff;
    --brand-purple: #4a2358;
    --text-dark: #1f1a22;
    --muted-purple: #6b4f78;
  }
  * { box-sizing: border-box; margin: 0; padding: 0; }
  html, body {
    width: 1200px; height: 799px; overflow: hidden;
    background: var(--page-bg);
    font-family: "Open Sans", Arial, sans-serif;
  }
  .business-card {
    position: absolute; left: 110px; top: 120px;
    width: 980px; height: 560px;
    background: var(--card-bg);
    box-shadow: 0 6px 22px rgba(40, 20, 50, 0.18);
  }
  .agent { position: absolute; color: var(--brand-purple); white-space: nowrap; }
  .agent-name { font-size: 36px; font-weight: 400; line-height: 1.05; }
  .agent-detail { font-size: 16px; line-height: 1.25; padding-left: 2px; }
  .agent--broker { left: 40px; top: 30px; }
  .agent--realtor { right: 40px; top: 120px; }

  .brand {
    position: absolute; left: 0; right: 0; top: 218px;
    display: flex; justify-content: center; align-items: center; gap: 18px;
  }
  .brand-mark { width: 44px; height: 44px; border-radius: 50%; background: var(--brand-purple); flex-shrink: 0; }
  .brand-name { font-size: 52px; font-weight: 600; color: var(--brand-purple); letter-spacing: 1px; white-space: nowrap; }
  .office-number {
    position: absolute; left: 0; right: 0; top: 302px;
    text-align: center; font-size: 17px; color: var(--muted-purple);
  }

  .contact-row {
    position: absolute; left: 40px; right: 40px; bottom: 44px;
    display: flex; justify-content: space-between; align-items: center;
  }
  .contact-item {
    display: flex; align-items: center; gap: 14px;
    color: var(--text-dark); font-size: 14px; line-height: 1.35; white-space: nowrap;
  }
  .contact-address { font-style: normal; }
  .contact-icon {
    width: 36px; height: 36px; border-radius: 50%; background: var(--brand-purple);
    display: flex; align-items: center; justify-content: center; flex-shrink: 0;
  }
  .contact-icon svg { width: 20px; height: 20px; }
</style>
</head>
<body>
  <main class="business-card">
    <section class="agent agent--broker">
      <h2 class="agent-name">Marla Halvern</h2>
      <p class="agent-detail">Broker (555).316.4827</p>
    </section>

    <section class="agent agent--realtor">
      <h2 class="agent-name">Tessa Halvern</h2>
      <p class="agent-detail">Realtor (555).627.9154</p>
    </section>

    <div class="brand">
      <span class="brand-mark"></span>
      <h1 class="brand-name">Halvern Properties</h1>
    </div>
    <p class="office-number">Office #: (555).841.2600</p>

    <footer class="contact-row">
      <div class="contact-item contact-item--address">
        <span class="contact-icon">
          <svg viewBox="0 0 24 24"><path d="M12 2a7 7 0 0 0-7 7c0 5 7 13 7 13s7-8 7-13a7 7 0 0 0-7-7zm0 9.5A2.5 2.5 0 1 1 12 6.5a2.5 2.5 0 0 1 0 5z" fill="#fff"/></svg>
        </span>
        <address class="contact-address">518B W. Cottonwell Ave.<br>Cedar Hollow, TX. 70999</address>
      </div>
      <div class="contact-item contact-item--email">
        <span class="contact-icon">
          <svg viewBox="0 0 24 24"><rect x="3" y="6" width="18" height="12" rx="1.5" fill="#fff"/><path d="M3.5 7l8.5 6 8.5-6" stroke="#4a2358" stroke-width="1.6" fill="none"/></svg>
        </span>
        <span>halvern@halvernproperties-example.com</span>
      </div>
      <div class="contact-item contact-item--web">
        <span class="contact-icon">
          <svg viewBox="0 0 24 24" fill="none" stroke="#fff" stroke-width="1.6"><circle cx="12" cy="12" r="8.5"/><ellipse cx="12" cy="12" rx="3.8" ry="8.5"/><path d="M3.5 12h17M5 7.5h14M5 16.5h14"/></svg>
        </span>
        <span>halvernproperties-example.com</span>
      </div>
    </footer>
  </main>
</body>
</html>
```